TRESSLY FACEBOOK DESIGN

I need new design for facebook https://www.facebook.com/tresslyitalia.
Our Businnes is Hair care , hair replacement , hair transplant . hair regrowth . i NEED MEDICAL AND PROFESSIONAL DESIGN. I NEED ALSO RESPONSIVE DESIGN

Target Market(s)

Consumers

Industry/Entity Type

MEDICAL AND COSMETICS

Colors
0054AA
0677BA
7BADD7
CADEEF
E8F1F8

Requirements
Must have
• MEDICAL
Nice to have
• RESPONSIVE DESIGN

```html
<!DOCTYPE html>
<html lang="it">
<head>
<meta charset="utf-8">
<title>Tressly – Cura e reintegrazione dei capelli</title>
<link rel="stylesheet" href="https://fonts.googleapis.com/css2?family=Nunito:ital,wght@0,600;0,700;0,800;1,600&display=swap">
<style>
  :root {
    --brand-deep: #0054AA;
    --brand-mid: #0677BA;
    --brand-sky: #2EA6DD;
    --brand-soft: #7BADD7;
    --brand-pale: #CADEEF;
    --brand-mist: #E8F1F8;
    --white: #FFFFFF;
    --hair-dark: #3a2a22;
    --hair-light: #6b4d3c;
    --skin: #e9cdb8;
  }
  * { margin: 0; padding: 0; box-sizing: border-box; }
  html, body { width: 1200px; height: 527px; overflow: hidden; background: var(--white); }
  .cover {
    position: relative;
    width: 1200px;
    height: 527px;
    overflow: hidden;
    font-family: "Nunito", sans-serif;
  }
  .cover__art { position: absolute; inset: 0; width: 1200px; height: 527px; }
  .brand {
    position: absolute;
    left: 620px;
    top: 48px;
    display: flex;
    align-items: center;
    gap: 18px;
  }
  .brand__dot {
    width: 62px; height: 62px;
    border-radius: 50%;
    background: var(--brand-sky);
  }
  .brand__name {
    font-size: 82px;
    font-weight: 800;
    color: var(--brand-deep);
    line-height: 1;
    letter-spacing: 1px;
  }
  .tagline {
    position: absolute;
    left: 624px;
    top: 166px;
    font-size: 23px;
    font-weight: 700;
    color: var(--brand-deep);
    letter-spacing: 1px;
    text-transform: uppercase;
  }
  .hashtags {
    position: absolute;
    left: 706px;
    top: 296px;
    color: var(--white);
    font-size: 25px;
    font-style: italic;
    font-weight: 600;
    line-height: 38px;
    list-style: none;
  }
  .services {
    position: absolute;
    left: 628px;
    top: 398px;
    width: 470px;
    display: grid;
    grid-template-columns: 200px 270px;
    row-gap: 10px;
    list-style: none;
    color: var(--white);
    font-size: 25px;
    font-weight: 800;
  }
  .services li::before { content: "• "; }
</style>
</head>
<body>
<main class="cover">
  <svg class="cover__art" viewBox="0 0 1200 527" aria-hidden="false">
    <defs>
      <linearGradient id="portraitTone" x1="0" y1="0" x2="0.3" y2="1">
        <stop offset="0" stop-color="var(--hair-light)"/>
        <stop offset="0.45" stop-color="var(--hair-dark)"/>
        <stop offset="0.62" stop-color="var(--skin)"/>
        <stop offset="1" stop-color="var(--skin)"/>
      </linearGradient>
    </defs>
    <rect class="portrait" x="0" y="0" width="760" height="527" fill="url(#portraitTone)"
          role="img" aria-label="Foto di profilo di un uomo con capelli castani e attaccatura dei capelli evidenziata"/>
    <path class="panel-white" d="M460,0 Q575,110 600,280 L620,527 L1200,527 L1200,0 Z" fill="var(--white)"/>
    <path class="panel-edge" d="M460,0 Q575,110 600,280 L620,527" fill="none" stroke="var(--brand-sky)" stroke-width="6"/>
    <path class="wave-soft" d="M604,300 C700,260 780,330 900,300 C1010,272 1110,250 1200,268 L1200,527 L620,527 Z" fill="var(--brand-pale)"/>
    <path class="wave-main" d="M606,318 C710,280 790,345 905,318 C1015,292 1110,272 1200,288 L1200,527 L620,527 Z" fill="var(--brand-sky)"/>
    <path class="wave-light" d="M612,420 C760,390 900,440 1200,380 L1200,527 L620,527 Z" fill="var(--brand-mid)" opacity="0.25"/>
    <path class="tagline-swash" d="M640,212 C760,222 900,196 1040,206" fill="none" stroke="var(--brand-soft)" stroke-width="4" stroke-linecap="round"/>
  </svg>

  <div class="brand">
    <span class="brand__dot"></span>
    <span class="brand__name">Tressly</span>
  </div>
  <p class="tagline">Cura e reintegrazione dei capelli</p>

  <ul class="hashtags">
    <li>#capellifelici</li>
    <li>#semplicementemigliori</li>
  </ul>

  <ul class="services">
    <li>Hair care</li>
    <li>Hair replacement</li>
    <li>Hair transplant</li>
    <li>Hair regrowth</li>
  </ul>
</main>
</body>
</html>
```